Heritage Hollow Business Cards

Require a business card design. <br/><br/>Needs to include logo (either round or long version) plus these details:<br/>Maya Torvel<br/>Heritage Hollow<br/>maya@quonbrook.com.au<br/>02 6481 7390<br/>PO Box Glenwarra NSW 2913<br/>www.heritagehollow.com.au<br/><br/>I need in an editable format so that I can create for multiple staff members. <br/><br/>

Target Market(s)

We are an online store selling renovation products to home owners are builders. Looking for a classic classy design.

Industry/Entity Type

Home And Garden

Contact Information for Business Card

Maya Torvel
Heritage Hollow
maya@quonbrook.com.au
02 6481 7390
PO Box Glenwarra NSW 2913
www.heritagehollow.com.au

Colors

Designer to choose colors to be used in the design.

Requirements
Must have
• Must include Logo.

```html
<!DOCTYPE html>
<html lang="en">
<head>
<meta charset="utf-8">
<title>Heritage Hollow Business Cards</title>
<link href="https://fonts.googleapis.com/css2?family=Barlow:wght@400;500;600&display=swap" rel="stylesheet">
<style>
  :root {
    --backdrop: #5a5b5d;
    --card-front: #d1d2d3;
    --card-front-shade: #c8c9ca;
    --card-back: #ffffff;
    --ink: #231f20;
    --mark-tone: #3a3738;
    --sketch-tone: #e9e9ea;
    --sketch-tone-deep: #dcdcdd;
  }
  html, body {
    margin: 0;
    padding: 0;
    width: 1200px;
    height: 1000px;
    overflow: hidden;
    background: var(--backdrop);
  }
  .canvas {
    position: relative;
    width: 1200px;
    height: 1000px;
    font-family: "Barlow", Arial, sans-serif;
    color: var(--ink);
  }
  .card {
    position: absolute;
    border-radius: 30px 0 30px 30px;
    overflow: hidden;
  }
  .card--front {
    left: 166px;
    top: 385px;
    width: 428px;
    height: 229px;
    background: linear-gradient(160deg, var(--card-front), var(--card-front-shade));
  }
  .brand-mark {
    position: absolute;
    left: 184px;
    top: 52px;
    width: 62px;
    height: 62px;
    background: var(--mark-tone);
  }
  .brand-name {
    position: absolute;
    left: 152px;
    top: 124px;
    margin: 0;
    font-weight: 500;
    font-size: 25px;
    line-height: 26px;
    color: var(--ink);
  }
  .website {
    position: absolute;
    left: 152px;
    top: 201px;
    margin: 0;
    font-weight: 600;
    font-size: 9px;
    letter-spacing: 0.2px;
  }
  .card--back {
    left: 609px;
    top: 387px;
    width: 424px;
    height: 227px;
    background: var(--card-back);
  }
  .roof-sketch {
    position: absolute;
    left: 0;
    top: 0;
    width: 280px;
    height: 227px;
    background: linear-gradient(135deg, var(--sketch-tone-deep), var(--sketch-tone) 55%, var(--card-back));
  }
  .contact {
    position: absolute;
    left: 239px;
    top: 89px;
    margin: 0;
    font-style: normal;
    font-weight: 500;
    font-size: 9px;
    line-height: 11px;
    letter-spacing: 0.2px;
    color: var(--ink);
  }
</style>
</head>
<body>
<main class="canvas">
  <section class="card card--front" aria-label="Card front">
    <div class="brand-mark" role="img" aria-label="Heritage Hollow brand mark"></div>
    <h1 class="brand-name">Heritage<br>Hollow</h1>
    <p class="website">www.heritagehollow.com.au</p>
  </section>
  <section class="card card--back" aria-label="Card back">
    <div class="roof-sketch" role="img" aria-label="Faint pencil sketch of a gabled roof with a chimney"></div>
    <address class="contact">
      Maya Torvel<br>
      Heritage Hollow<br>
      maya@quonbrook.com.au<br>
      02 6481 7390<br>
      PO Box Glenwarra NSW 2913
    </address>
  </section>
</main>
</body>
</html>
```